Vardena General Painting Ltd. - Construction painting company providing high-quality service

We need a logo and business card design for a painting company that provides high-quality work for major developers and builders in Calgary, Alberta. Our projects include commercial high-rise residential towers. We would like designs that communicate professionalism and high quality service.
Updates
Need extra days to review
Target Market(s)
Developers and builders
Industry/Entity Type
Construction
Contact Information for Business Card
Company name, employee name, title, phone number, email address
Font styles to use
Colors
Designer to choose colors to be used in the design.
Look and feel
Each slider illustrates characteristics of the customer's brand and the style your logo design should communicate.

```html
<!DOCTYPE html>
<html lang="en">
<head>
<meta charset="utf-8">
<title>Vardena General Painting Ltd. — Business Card</title>
<link href="https://fonts.googleapis.com/css2?family=Montserrat:wght@600&family=Arimo:wght@400&display=swap" rel="stylesheet">
<style>
  :root {
    --page: #0c0c0d;
    --card: #27282b;
    --card-deep: #1f2023;
    --accent: #1ea3e6;
    --ink: #f2f3f5;
    --emboss: #36383c;
  }
  * { box-sizing: border-box; margin: 0; padding: 0; }
  html, body {
    width: 1200px; height: 820px; overflow: hidden;
    background: var(--page);
  }
  .canvas {
    width: 1200px; height: 820px;
    display: flex; align-items: center; justify-content: center; gap: 44px;
  }
  .card {
    position: relative;
    width: 540px; height: 310px;
    background: linear-gradient(160deg, var(--card), var(--card-deep));
    border-left: 3px solid var(--accent);
    border-bottom: 3px solid var(--accent);
    overflow: hidden;
  }
  /* Wordmark: one colour, one weight, two sizes */
  .wordmark {
    font-family: "Montserrat", sans-serif; font-weight: 600;
    color: var(--accent); text-transform: uppercase; white-space: nowrap;
  }
  .wordmark-name {
    display: block; font-size: 34px; line-height: 1; letter-spacing: 0.16em;
  }
  .wordmark-tag {
    display: block; font-size: 10.5px; line-height: 1; letter-spacing: 0.14em;
    margin-top: 7px; padding-left: 3px;
  }
  /* Front */
  .brand {
    position: absolute; top: 44px; left: 150px;
    display: flex; align-items: center; gap: 16px;
  }
  .brand-dot {
    flex: none; width: 62px; height: 62px; border-radius: 50%;
    border: 4px solid var(--accent);
  }
  .person { position: absolute; left: 40px; top: 150px; }
  .person-name {
    font-family: "Montserrat", sans-serif; font-weight: 600;
    font-size: 21px; line-height: 1.1; color: var(--accent); text-transform: uppercase;
  }
  .person-title {
    font-family: "Arimo", sans-serif; font-size: 14px;
    color: var(--ink); text-transform: uppercase; margin-top: 3px;
  }
  .rule {
    position: absolute; left: 40px; right: 30px; top: 205px;
    height: 1px; background: var(--accent);
  }
  .contacts {
    position: absolute; left: 40px; top: 222px;
    list-style: none;
    font-family: "Arimo", sans-serif; font-size: 14px; color: var(--ink);
  }
  .contacts li { display: flex; align-items: center; gap: 10px; line-height: 24px; }
  .contacts svg { width: 16px; height: 16px; flex: none; }
  .website {
    position: absolute; right: 30px; top: 226px;
    font-family: "Arimo", sans-serif; font-size: 14px; color: var(--ink);
    text-transform: uppercase;
  }
  .website .domain { color: var(--accent); }
  /* Back */
  .back-circle {
    position: absolute; left: 46px; top: 52px;
    width: 200px; height: 200px; border-radius: 50%;
    border: 6px solid var(--emboss);
  }
  .card-back .wordmark {
    position: absolute; right: 34px; top: 128px;
  }
</style>
</head>
<body>
<main class="canvas">
  <section class="card card-front" aria-label="Business card front">
    <div class="brand">
      <span class="brand-dot" aria-hidden="true"></span>
      <p class="wordmark"><span class="wordmark-name">Vardena</span><span class="wordmark-tag">General Painting Ltd.</span></p>
    </div>
    <div class="person">
      <p class="person-name">Daniel Mercer</p>
      <p class="person-title">Managing Director</p>
    </div>
    <div class="rule"></div>
    <ul class="contacts">
      <li>
        <svg viewBox="0 0 24 24" fill="none" stroke="var(--accent)" stroke-width="2.2" stroke-linecap="round" stroke-linejoin="round"><path d="M22 16.9v3a2 2 0 0 1-2.2 2 19.8 19.8 0 0 1-8.6-3.1 19.5 19.5 0 0 1-6-6A19.8 19.8 0 0 1 2.1 4.2 2 2 0 0 1 4.1 2h3a2 2 0 0 1 2 1.7c.1 1 .4 1.9.7 2.8a2 2 0 0 1-.5 2.1L8 9.9a16 16 0 0 0 6 6l1.3-1.3a2 2 0 0 1 2.1-.4c.9.3 1.8.6 2.8.7a2 2 0 0 1 1.7 2z"/></svg>
        <span>044-555 210 347</span>
      </li>
      <li>
        <svg viewBox="0 0 24 24" fill="none" stroke="var(--accent)" stroke-width="2.2" stroke-linejoin="round"><rect x="2" y="5" width="20" height="14"/><path d="M2 5l10 8 10-8"/></svg>
        <span>INFO@VARDENAPAINT.COM</span>
      </li>
    </ul>
    <p class="website">www.<span class="domain">vardenapainting</span>.com</p>
  </section>

  <section class="card card-back" aria-label="Business card back">
    <span class="back-circle" aria-hidden="true"></span>
    <p class="wordmark"><span class="wordmark-name">Vardena</span><span class="wordmark-tag">General Painting Ltd.</span></p>
  </section>
</main>
</body>
</html>
```